The Varnel Cipher: Book Cover

I need a book cover for the English language version of a counterfactual history thriller, a story that takes off where "Greymarch" by Dalton Pike ends.

1983: Germany has won the war, the postwar time has brought prosperity and peace to Europe. The Wild East is no longer wild, only beyond the Urals do scattered Soviet units still occasionally carry out attacks against the Grenzwall administration and German settlers.
Lukas Brenning, born in Stuttgart and a criminalist with heart and soul, is district chief in Hartmannstadt a.d. Medritz, and thus simultaneously the highest police officer, judge, representative of the Reich and the KV. Ten years earlier, he had been transferred to the eastern border of the Reich in order to avoid the unpleasant consequences of his investigations into the machinations of some high-ranking Ordist party members in southern Germany. Brenning likes working in the east, but even here he can't keep his investigator's instincts in check. When a mysterious stranger turns up, Brenning's investigation brings strange things to light. The Veltrax provide the necessary information, but at the same time prevent further investigations by the KV. Despite a warning from his superiors, Brenning cannot let the file rest. When he comes across a well-kept secret about the 1940 peace treaty between Germany, England and France, events take a turn for the worse.
Brenning finds himself on the wrong side of a manhunt which he can only survive with the help of an unlikely ally.

The novel has appeared in German a couple of years ago. I need a book cover for an English language softcover book and an eBook addressed at English speakers. Please, even though the Grenzwall and Ordist party are mentioned: no swastikas and no openly National Socialist symbols.

Target Market(s)

all English speakers accross the world

Requirements
Should not have
• Swastikas and other offensive signs of the Nazi reign

```html
<!DOCTYPE html>
<html lang="en">
<head>
<meta charset="utf-8">
<title>The Varnel Cipher – Book Cover</title>
<link rel="stylesheet" href="https://fonts.googleapis.com/css2?family=Jost:wght@600&family=Stardos+Stencil:wght@700&display=swap">
<style>
  :root {
    --desk-dark: #1c130d;
    --desk-mid: #3a2819;
    --desk-warm: #4a3322;
    --map-tone: #e0ae72;
    --map-sea: #b9c2aa;
    --map-edge: #e4dcc6;
    --paper-light: #cbbfa3;
    --paper-shade: #8f8472;
    --folder: #c59c71;
    --folder-light: #cfa881;
    --folder-edge: #a97e57;
    --stamp-red: #b20b0b;
    --ink: #2e2620;
    --white: #ffffff;
    --gun: #23262c;
    --gun-light: #3b414b;
  }
  * { margin: 0; padding: 0; box-sizing: border-box; }
  html, body { width: 750px; height: 1200px; overflow: hidden; background: var(--desk-dark); }
  .cover {
    position: relative;
    width: 750px;
    height: 1200px;
    overflow: hidden;
    background:
      radial-gradient(ellipse at 50% 55%, rgba(90,62,40,0.55) 0%, rgba(0,0,0,0) 65%),
      linear-gradient(175deg, var(--desk-warm) 0%, var(--desk-mid) 45%, var(--desk-dark) 100%);
  }
  .scene { position: absolute; inset: 0; }
  .folder {
    position: absolute;
    left: 78px; top: 171px;
    width: 606px; height: 879px;
    background:
      radial-gradient(ellipse at 55% 40%, var(--folder-light) 0%, var(--folder) 55%, var(--folder-edge) 100%);
    box-shadow: 0 10px 30px rgba(0,0,0,0.6), 0 0 4px rgba(0,0,0,0.4);
    border-radius: 3px 6px 4px 3px;
  }
  .author {
    position: absolute;
    left: 0; right: 0; top: 212px;
    padding-left: 10px;
    text-align: center;
    font-family: "Jost", sans-serif;
    font-weight: 600;
    font-size: 36px;
    letter-spacing: 5px;
    line-height: 1;
    color: var(--white);
  }
  .emblem-area {
    position: absolute;
    left: 259px; top: 330px;
    width: 232px; height: 81px;
    background: radial-gradient(ellipse at center, rgba(46,38,32,0.45) 0%, rgba(46,38,32,0) 75%);
  }
  .title {
    position: absolute;
    left: 95px; top: 478px;
    width: 600px;
    transform: rotate(-9deg);
    transform-origin: center;
    font-family: "Stardos Stencil", sans-serif;
    font-weight: 700;
    color: var(--stamp-red);
    text-align: center;
    line-height: 0.9;
  }
  .title .small { display: block; font-size: 58px; margin-left: -40px; }
  .title .big { display: block; font-size: 112px; letter-spacing: 2px; }
  .title .big.first { margin-left: -30px; }
  .title .big.second { margin-left: -90px; }
  .form-lines {
    position: absolute;
    left: 155px; width: 463px; top: 0;
  }
  .form-lines span {
    position: absolute; left: 0; right: 0;
    height: 3px; background: var(--ink);
  }
</style>
</head>
<body>
<div class="cover">
  <svg class="scene" width="750" height="1200" viewBox="0 0 750 1200">
    <defs>
      <linearGradient id="mapFill" x1="0" y1="0" x2="1" y2="1">
        <stop offset="0" stop-color="var(--map-tone)"/>
        <stop offset="0.7" stop-color="var(--map-tone)"/>
        <stop offset="1" stop-color="var(--map-sea)"/>
      </linearGradient>
      <linearGradient id="paperFill" x1="0" y1="0" x2="1" y2="1">
        <stop offset="0" stop-color="var(--paper-light)"/>
        <stop offset="1" stop-color="var(--paper-shade)"/>
      </linearGradient>
      <filter id="soft"><feGaussianBlur stdDeviation="2"/></filter>
    </defs>
    <polygon role="img" aria-label="Old paper map of eastern Europe and Russia" points="0,0 446,0 555,172 90,470 0,488" fill="url(#mapFill)" stroke="var(--map-edge)" stroke-width="5" filter="url(#soft)"/>
    <polygon role="img" aria-label="Old hand-drawn document sheet" points="600,0 750,0 750,100 690,88 630,40" fill="url(#paperFill)" filter="url(#soft)"/>
    <polygon role="img" aria-label="Sheets of technical plans" points="684,560 750,520 750,960 684,990" fill="url(#paperFill)" filter="url(#soft)"/>
  </svg>

  <div class="folder"></div>

  <p class="author">JONAS HALLERBERG</p>

  <div class="emblem-area" role="img" aria-label="Eagle emblem printed on the folder"></div>

  <h1 class="title">
    <span class="small">THE</span>
    <span class="big first">VARNEL</span>
    <span class="big second">CIPHER</span>
  </h1>

  <div class="form-lines">
    <span style="top:853px"></span>
    <span style="top:901px"></span>
    <span style="top:947px"></span>
  </div>

  <svg class="scene" width="750" height="1200" viewBox="0 0 750 1200">
    <defs>
      <linearGradient id="gunFill" x1="1" y1="0" x2="0" y2="1">
        <stop offset="0" stop-color="var(--gun-light)"/>
        <stop offset="1" stop-color="var(--gun)"/>
      </linearGradient>
      <filter id="gunSoft"><feGaussianBlur stdDeviation="1.5"/></filter>
    </defs>
    <path role="img" aria-label="Pistol lying on the desk" d="M280,1200 L310,1100 L470,1060 L540,1030 L560,1050 L600,1040 L640,980 L750,900 L750,1200 Z" fill="url(#gunFill)" filter="url(#gunSoft)"/>
  </svg>
</div>
</body>
</html>
```